Card Design for my dog training business RB Paws Training

Need a business card design for my dog training business with my new logo. Want the card to come off professional yet fun. Want it to be very eye catchy as well. I normally have these at vet clinics, pet stores, and groomers. so need it to look better than my competitors.
Target Market(s)
dog owners
Industry/Entity Type
Dog Training
Contact Information for Business Card
needs logo, my name and info
Font styles to use
Serif
Colors
0255a3
ffffff
ec1f27
000000
333333
fbfbfb
Requirements
Must have
- RB Paws Training
- Lydia Fensworth
- 555 390 2176
- info@rbpawstraining.example
- www.rbpawstraining.example

```html
<!DOCTYPE html>
<html lang="en">
<head>
<meta charset="utf-8">
<title>RB Paws Training — Business Card</title>
<link rel="stylesheet" href="https://fonts.googleapis.com/css2?family=EB+Garamond:ital@1&family=Open+Sans:wght@400;600;700&display=swap">
<style>
  :root {
    --backdrop: #3b322d;
    --card: #1b1d1f;
    --card-edge: #111213;
    --ink: #fbfbfb;
    --foil: #9a9c9e;
    --rule: #8d8f91;
  }
  html, body {
    margin: 0;
    width: 1200px;
    height: 864px;
    overflow: hidden;
    background: var(--backdrop);
  }
  .canvas {
    position: relative;
    width: 1200px;
    height: 864px;
  }
  .card {
    position: absolute;
    width: 520px;
    height: 300px;
    background: var(--card);
    border-radius: 3px;
    box-shadow: 0 14px 28px rgba(0,0,0,.45);
    box-sizing: border-box;
  }
  /* Front */
  .card--front { left: 60px; top: 120px; }
  .card--front .brand {
    position: absolute;
    left: 0; right: 0; top: 92px;
    text-align: center;
    font-family: "Open Sans", sans-serif;
    font-weight: 600;
    font-size: 34px;
    color: var(--foil);
  }
  .card--front .tagline {
    position: absolute;
    left: 0; right: 0; top: 196px;
    text-align: center;
    font-family: "EB Garamond", serif;
    font-style: italic;
    font-size: 19px;
    color: var(--foil);
  }
  /* Back */
  .card--back { left: 620px; top: 444px; }
  .card--back .brand {
    position: absolute;
    left: 28px; width: 210px; top: 118px;
    text-align: center;
    font-family: "Open Sans", sans-serif;
    font-weight: 600;
    font-size: 24px;
    line-height: 1.2;
    color: var(--ink);
  }
  .card--back .divider {
    position: absolute;
    left: 262px; top: 70px;
    width: 1px; height: 160px;
    background: linear-gradient(transparent, var(--rule) 20%, var(--rule) 80%, transparent);
  }
  .contact {
    position: absolute;
    left: 286px; top: 96px;
    font-family: "Open Sans", sans-serif;
    color: var(--ink);
  }
  .contact__name {
    margin: 0 0 12px;
    font-weight: 700;
    font-size: 21px;
  }
  .contact__list {
    list-style: none;
    margin: 0; padding: 0;
    font-size: 14px;
    line-height: 23px;
  }
  .contact__list li { display: flex; align-items: center; gap: 8px; }
  .contact__list svg { width: 13px; height: 13px; fill: var(--ink); flex: none; }
</style>
</head>
<body>
<main class="canvas">
  <section class="card card--front" aria-label="Business card front">
    <div class="brand">RB Paws Training</div>
    <p class="tagline">“Training dogs across Texas one dog at a time.”</p>
  </section>

  <section class="card card--back" aria-label="Business card back">
    <div class="brand">RB Paws Training</div>
    <div class="divider"></div>
    <div class="contact">
      <h1 class="contact__name">Lydia Fensworth</h1>
      <ul class="contact__list">
        <li>
          <svg viewBox="0 0 16 16" aria-hidden="true"><path d="M3.6 1.2l2.3 2.6-1.3 1.8c.9 2 2.6 3.8 4.7 4.8l1.8-1.3 2.6 2.3-1.3 2.2C7.6 13.9 2.2 8.4 1.4 2.5z"/></svg>
          555 390 2176
        </li>
        <li>
          <svg viewBox="0 0 16 16" aria-hidden="true"><path d="M1 3h14v10H1z M2 4.2v.4l6 4.2 6-4.2v-.4z" fill-rule="evenodd"/></svg>
          info@rbpawstraining.example
        </li>
        <li>
          <svg viewBox="0 0 16 16" aria-hidden="true"><circle cx="8" cy="8" r="7"/><path d="M1 8h14M8 1c-3 3.5-3 10.5 0 14M8 1c3 3.5 3 10.5 0 14" stroke="#1b1d1f" stroke-width="1" fill="none"/></svg>
          www.rbpawstraining.example
        </li>
      </ul>
    </div>
  </section>
</main>
</body>
</html>
```